Cool blackchain based app company needs a website :)

pillcheckhub.net

Kinda says it all!! This is an app which sits on your smartfone / tablet. You scan a QR code from a medicinal product and our app will verify if the product you have is genuine. It's simple, It's free.

The design could be very modern and simple. It should show in graphical form how the app works and have FAQ's etc.

pillcheckhub.net is designed specifically to allow consumers verify that the medical products which they have purchased are genuine.

Detailed brief with content attached. Logo in high res and QR code attached.

Full website required.
Updates

Target Market(s)

Pharmaceutical

Industry/Entity Type

Pharmaceutical

Coding

Coded - Design and coding required

Number of Pages Required

3 page

Colors

Designer to choose colors to be used in the design.

Requirements
Must have
• Strong visuals - very simple navigation - 3 pages
Nice to have
• Animation of the process
Should not have
• Jargon!

```html
<!DOCTYPE html>
<html lang="en">
<head>
<meta charset="utf-8">
<title>pillcheckhub.net — Verify your medicine</title>
<link href="https://fonts.googleapis.com/css2?family=Roboto:wght@300;400;500;700&family=Kaushan+Script&display=swap" rel="stylesheet">
<style>
:root{
  --green:#7cb41c;
  --blue:#1f72c0;
  --ink:#333;
  --muted:#555;
  --band:#2a2a2a;
  --navy:#1c2a4b;
  --navy-deep:#14203c;
  --light:#f1f2f4;
  --white:#fff;
}
*{box-sizing:border-box;margin:0;padding:0}
html,body{width:1200px;height:3352px;overflow:hidden}
body{font-family:'Roboto',Arial,sans-serif;color:var(--ink);background:var(--white);position:relative}
section,header,footer{position:absolute;left:0;width:1200px}

/* Hero */
.hero{top:0;height:548px;overflow:hidden}
.hero-photo{position:absolute;inset:0;background:linear-gradient(100deg,#5b5a57 0%,#8a8c8f 35%,#b7bcc3 60%,#9aa1aa 100%)}
.hero-shade{position:absolute;inset:0;background:rgba(20,24,32,.25)}
.nav{position:absolute;top:0;left:0;width:1200px;height:70px}
.brand-dot{position:absolute;left:42px;top:12px;width:44px;height:44px;border-radius:50%;background:var(--white)}
.nav-links{position:absolute;left:118px;top:26px;display:flex;gap:0;list-style:none}
.nav-links li{color:var(--white);font-size:14px;margin-right:38px}
.btn-outline,.btn-solid{position:absolute;top:18px;height:34px;border-radius:17px;font-size:13px;line-height:32px;text-align:center;font-weight:500}
.btn-outline{left:926px;width:108px;border:1.5px solid var(--white);color:var(--white)}
.btn-solid{left:1044px;width:112px;background:var(--white);color:#222;border:1.5px solid var(--white)}
.hero-copy{position:absolute;top:188px;left:0;width:1200px;text-align:center;color:var(--white)}
.hero-copy h1{font-family:'Kaushan Script',cursive;font-weight:400;font-size:36px;letter-spacing:1px}
.hero-copy p{font-size:14px;line-height:22px;margin-top:12px}
.hero-cta{display:inline-block;margin-top:20px;border:1.5px solid var(--white);border-radius:5px;padding:8px 14px;font-size:14px}

/* Steps */
.steps{top:548px;height:105px;background:var(--band);color:var(--white)}
.step{position:absolute;top:28px;width:330px;display:flex;align-items:center;gap:20px;font-size:14px;line-height:20px}
.step-num{flex:0 0 44px;height:44px;border:1.5px solid var(--white);border-radius:50%;text-align:center;line-height:41px;font-size:13px}

/* Intro */
.intro{top:653px;height:268px;text-align:center}
.title-green{color:var(--green);font-size:48px;font-weight:700}
.title-blue{color:var(--blue);font-size:38px;font-weight:700}
.intro .title-green{margin-top:14px}
.intro p{font-size:15px;color:var(--muted);margin-top:24px;line-height:24px;padding:0 70px}

/* Authenticity */
.authentic{top:921px;height:492px;overflow:hidden}
.authentic-photo{position:absolute;inset:0;background:linear-gradient(90deg,#3a3f46 0%,#55595f 45%,#8d9096 70%,#6f737a 100%)}
.authentic-copy{position:absolute;left:88px;top:56px;width:600px;color:var(--white)}
.authentic-copy h2{font-size:40px;font-weight:400;margin-bottom:18px}
.authentic-copy p{font-size:14px;font-weight:500;line-height:21px;margin-bottom:20px}

/* Anonymity / Safety */
.feature{text-align:center}
.anonymity{top:1413px;height:402px}
.anonymity .title-green{margin-top:18px}
.feature-icon{display:block;margin:8px auto 6px}
.feature p{font-size:15px;color:var(--muted);line-height:24px;margin-top:22px;padding:0 70px}
.anonymity p + p{margin-top:22px}

/* Security */
.security{top:1815px;height:494px;background:radial-gradient(circle at 30% 50%,#22345c 0%,var(--navy) 50%,var(--navy-deep) 100%)}
.globe{position:absolute;left:130px;top:70px;width:350px;height:350px;border-radius:50%;background:radial-gradient(circle at 45% 45%,rgba(120,170,235,.35) 0%,rgba(70,110,180,.18) 55%,rgba(28,42,75,0) 72%)}
.security-copy{position:absolute;left:612px;top:86px;width:520px;color:var(--white)}
.security-copy h2{font-size:26px;font-weight:500;margin-bottom:4px}
.security-copy p{font-size:14px;font-weight:500;line-height:21px;margin-bottom:20px}

/* Safety */
.safety{top:2309px;height:552px}
.safety .title-green{margin-top:22px}
.safety p{font-size:14.5px;line-height:23px;margin-top:18px;padding:0 67px}
.safety p:first-of-type{margin-top:26px}

/* Like bar */
.like-bar{top:2861px;height:80px;background:var(--light)}
.like-pill{position:absolute;left:380px;top:18px;width:447px;height:46px;background:var(--white);border-radius:23px;border:1px solid #e2e4e8}
.like-dot{position:absolute;left:20px;top:13px;width:20px;height:20px;border-radius:50%;background:#e4e6ea}
.like-btn{position:absolute;left:118px;top:13px;width:48px;height:20px;border-radius:3px;background:var(--blue);color:var(--white);font-size:11px;line-height:20px;text-align:center;font-weight:700}
.like-text{position:absolute;left:174px;top:15px;font-size:11px;color:#444}

/* Footer */
.site-footer{top:2941px;height:411px}
.col{position:absolute;top:48px}
.col h3{font-size:20px;font-weight:500;color:#222;margin-bottom:20px}
.col p{font-size:13px;line-height:20px;color:#333;margin-bottom:14px}
.contact-col{left:51px;width:250px}
.socials{display:flex;gap:14px;margin-top:4px}
.socials span{width:12px;height:12px;border-radius:50%;background:#222}
.mail-col{left:335px;width:532px}
.mail-col h3{text-align:center}
.field{border:1px solid #bbb;border-radius:3px;height:32px;font-size:12px;color:#888;padding:8px 12px;margin-bottom:14px}
.field-row{display:flex;gap:18px}
.field-row .field{flex:1}
.field-msg{height:66px}
.send-btn{display:block;width:136px;margin:6px auto 0;background:#222;color:var(--white);font-size:12px;font-weight:700;text-align:center;height:30px;line-height:30px;border-radius:3px}
.about-col{left:896px;width:260px}
.about-col p{color:#555}
.footer-base{position:absolute;top:351px;left:51px;width:1100px;border-top:1px solid #999;height:60px}
.copyright,.rights{position:absolute;top:28px;font-size:12px;color:#222}
.rights{right:0}
.base-brand{position:absolute;left:420px;top:18px;display:flex;align-items:center;gap:8px;font-size:26px;font-weight:700;color:var(--blue)}
.base-brand span.mark{width:26px;height:26px;border-radius:50%;background:var(--green)}
</style>
</head>
<body>

<header class="hero">
  <div class="hero-photo" role="img" aria-label="Photo of a man in a checked shirt reading his phone in a bright kitchen"></div>
  <div class="hero-shade"></div>
  <nav class="nav">
    <div class="brand-dot" aria-label="pillcheckhub"></div>
    <ul class="nav-links">
      <li>Our Company</li><li>Our Team</li><li>FAQ's</li><li>Support</li><li>Contact Us</li>
    </ul>
    <div class="btn-outline">Scan QR Code</div>
    <div class="btn-solid">Download APP</div>
  </nav>
  <div class="hero-copy">
    <h1>Its Quick, Its Secure, Its Free</h1>
    <p>30% of all medicine bought online is counterfeit<br>Are you sure that the medication you take is genuine?</p>
    <div class="hero-cta">Scan a QR Code</div>
  </div>
</header>

<section class="steps">
  <div class="step" style="left:66px"><span class="step-num">1</span><span>Download PillCheckHub App in your Phone or Tablet</span></div>
  <div class="step" style="left:430px"><span class="step-num">2</span><span>Scan the QR code with your phone or tablet using your pillcheckhub app</span></div>
  <div class="step" style="left:794px"><span class="step-num">3</span><span>If it is a valid code then the product details will be displayed in the app on your device</span></div>
</section>

<section class="intro">
  <h2 class="title-green">Be Safe, Authenticate</h2>
  <h2 class="title-blue">Protect your health with pillcheckhub</h2>
  <p>Scan the pillcheckhub QR code which is printed on your medication using your phone or tablet</p>
  <p>pillcheckhub will authenticate your medicine against the manufacturers own production records and pillcheckhub will tell you immediately if your medicine is genuine</p>
</section>

<section class="authentic">
  <div class="authentic-photo" role="img" aria-label="Photo of a young woman working at a laptop in an office"></div>
  <div class="authentic-copy">
    <h2>Guaranteed Authenticity</h2>
    <p>Pillcheckhub has a unique and highly secure Blockchain database which contains details of billions of batches of medicines manufactured across the world</p>
    <p>Each time a manufacturer produces a batch of medicine, they send the details of that product to our secure Blockchain database. Our database records details of that batch of medicine and issues a unique encrypted QR code for every single batch. This code is printed on the medicine packet and it's packaging</p>
    <p>You simply scan the QR code from your meds using your phone or tablet. The pillcheckhub app unencrypts this code, verifies it against the details provided by the manufacturer and confirms if the medication is genuine or not directly to you on your device</p>
  </div>
</section>

<section class="feature anonymity">
  <h2 class="title-green">Guaranteed</h2>
  <svg class="feature-icon" width="70" height="106" viewBox="0 0 70 106" fill="none" stroke="#2f86d0" stroke-width="3">
    <path d="M12 44 V26 a23 23 0 0 1 46 0 v4"/>
    <rect x="4" y="44" width="62" height="58" rx="3"/>
    <circle cx="35" cy="66" r="6"/>
    <path d="M35 72 v12"/>
  </svg>
  <h2 class="title-blue">Anonymity</h2>
  <p>Your health and personal information are yours, and only yours!</p>
  <p>pillcheckhub does NOT record any personal or health information</p>
  <p>You don't have to log on to pillcheckhub and we don't ask you to register</p>
</section>

<section class="security">
  <div class="globe" role="img" aria-label="Illustration of a glowing network globe of connected points"></div>
  <div class="security-copy">
    <h2>Guaranteed Security</h2>
    <p>pillcheckhub are the first and only company in the world to use a (patent pending) encrypted specifically designed secure Blockchain database architecture for asset recording and authentication</p>
    <p>A Blockchain database is made up of a large network of independent database servers, each of which are in sync with each other. As soon as a record is appended to the database, all instances of the database simultaneously update</p>
    <p>Every record added to the database must contain encrypted keys before it is accepted by the Blockchain database. These keys form an interlinking chain</p>
    <p>This multitude of in-sync databases and verified-chain data structure makes the pillcheckhub database impossible to hack</p>
  </div>
</section>

<section class="feature safety">
  <h2 class="title-green">Guaranteed</h2>
  <svg class="feature-icon" width="110" height="100" viewBox="0 0 110 100" fill="none" stroke="#4a97d8" stroke-width="2.5" stroke-linejoin="round">
    <path d="M55 4 C38 12 22 14 8 12 V50 C8 72 30 90 55 96 C80 90 102 72 102 50 V12 C88 14 72 12 55 4 Z"/>
    <path d="M30 62 a12 12 0 0 1 4-23 a17 17 0 0 1 32-6 a13 13 0 0 1 14 15 a8 8 0 0 1-2 14 Z"/>
  </svg>
  <h2 class="title-blue">Safety</h2>
  <p>If you are taking medication you are doing so for a specific reason. It is imperative that your medication has been produced in accordance with strict international standards and that your medication contains the correct medicinal dosage</p>
  <p>The international pharmaceutical industry carefully manages their production processes to ensure the highest standards of product manufacture, production and distribution</p>
  <p>However, as in many industries, counterfeiting is a high value business. Counterfeit medicines cost the pharmaceutical industry more than €110 billion annually, €110 billion which otherwise would be invested into medical research and treatment development</p>
  <p>The financial cost is nothing compared to the loss of life. More than one million people's lives are lost each year due to counterfeit drugs. Counterfeit medicine often contains no active medicinal content or can contain a dangerous mix of ingredients. Whatever the mix, the medicine is not what it is claimed to be and the consequences of taking it can be lethal</p>
</section>

<section class="like-bar">
  <div class="like-pill">
    <span class="like-dot"></span>
    <span class="like-btn">Like</span>
    <span class="like-text">You and 4k others like this.</span>
  </div>
</section>

<footer class="site-footer">
  <div class="col contact-col">
    <h3>Contact Us</h3>
    <p>Please feel free to contact us for any issue. Our staff is available to you from 9AM until 5PM on weekdays.</p>
    <p><strong>Phone:</strong> +1 555 010 4477</p>
    <p><strong>Office:</strong> You Company Address</p>
    <p><strong>Email:</strong> hello@pillcheckhub.net</p>
    <div class="socials"><span></span><span></span><span></span><span></span><span></span></div>
  </div>
  <div class="col mail-col">
    <h3>Feel Free to Mail</h3>
    <div class="field-row"><div class="field">Name *</div><div class="field">Email *</div></div>
    <div class="field">Subject</div>
    <div class="field field-msg">Write Your Message Here...</div>
    <div class="send-btn">SEND MESSAGE</div>
  </div>
  <div class="col about-col">
    <h3>About Team</h3>
    <p>Our small team builds simple tools that help people check their medicine quickly, safely and without any sign up or personal data.</p>
    <p>We work with makers and pharmacies to keep every batch record accurate, current and easy to verify from any phone.</p>
  </div>
  <div class="footer-base">
    <span class="copyright">Copyright © PillCheckHub Inc</span>
    <span class="base-brand"><span class="mark"></span>pillcheckhub.net</span>
    <span class="rights">All rights reserved</span>
  </div>
</footer>

</body>
</html>
```